Ordinary Velvet Sparrow inquiring into the Mystery of her Heart needs a Book Cover design

Hello! I need a book cover design (for printed softcover 6” x 9” and eBook) for my new book titled "The Wide Season of a Modest Velvet Sparrow: Notes on Finding Room for Every Part." It's the story of a mom juggling a demanding technology career who embarks upon a self-discovery journey, faces cancer, and learns to expand her life, one vulnerable nibble at a time. With the help of a guide on her spiritual path, she learns to let go of her strong woman do-it-all persona, allowing her soul to fully shine. My purpose in writing the book is to share what I've learned about finding the "moreness" in being human.
*I would like to see book cover designs that communicate a sense of both strength and vulnerability, confidence and humbleness, curiosity and inner discovery—hinting at what's to come. I’ve uploaded a few images that I like because they feel clean and simple, and because they can be interpreted as metaphors of the beauty and power within each of us.
*If your design submission includes a mirror reflection of some sort of a “velvet sparrow” image that people are familiar with, then I would like it to convey a reluctant or questioning velvet sparrow, rather than a bold, fighting-to-save-the-world velvet sparrow.
*I lean toward a clean and calming background, as the book is really an inquiry into the mystery of this heart. It’s an examination of what I might have lost of myself, and ultimately gained, through all my crazy years of juggling. So, it’s a journey of spiritual growth.
Thank you for your interest and sharing your creative talent.

Target Market(s)

(1) Career-oriented parents, especially moms, who are in their 30's and 40's, in the midst of the struggle of trying to juggle it all; (2) life-long strivers, age 55+, who are finally slowing down and looking back to try and make sense of their lives, seeking to understand their buried inner life

Industry/Entity Type

Book Categories: Women & Business; Spiritual Self-help; Strong Women

Font styles to use
Serif

Colors

Designer to choose colors to be used in the design.

Requirements
Must have
• Clean and simple overall feeling
Nice to have
• I am open to including color—if so, perhaps some (not too much) hunter green would be nice (not required, but I’ve used it in a draft website design and rather like it).
Should not have
• Should not feel too "busy"

```html
<!DOCTYPE html>
<html lang="en">
<head>
<meta charset="utf-8">
<title>The Wide Season of a Modest Velvet Sparrow — Book Cover</title>
<link rel="stylesheet" href="https://fonts.googleapis.com/css2?family=Cinzel:wght@400;700&display=swap">
<style>
  :root {
    --page-bg: #e4e4e4;
    --cover-night: #021d1a;
    --figure-green: #50ee72;
    --mint-glow: #a4f7dc;
    --ground-green: #2f9a3b;
    --ground-deep: #2a5a2c;
    --ink-forest: #05392d;
    --title-white: #ffffff;
  }
  html, body {
    margin: 0;
    padding: 0;
    width: 1200px;
    height: 999px;
    overflow: hidden;
    background: var(--page-bg);
  }
  .book-cover {
    position: absolute;
    left: 300px;
    top: 50px;
    width: 600px;
    height: 900px;
    background: var(--cover-night);
    overflow: hidden;
    font-family: "Cinzel", "Times New Roman", serif;
  }
  .artwork-field {
    position: absolute;
    inset: 0;
    background:
      linear-gradient(to bottom,
        rgba(164, 247, 220, 0) 64%,
        rgba(164, 247, 220, 0.75) 75%,
        var(--ground-green) 86%,
        var(--ground-deep) 100%),
      radial-gradient(ellipse 330px 470px at 50% 42%,
        var(--figure-green) 0%,
        var(--figure-green) 62%,
        var(--cover-night) 100%);
  }
  .title-block {
    position: absolute;
    left: 0;
    right: 0;
    top: 200px;
    text-align: center;
    color: var(--ink-forest);
  }
  .kicker {
    margin: 0;
    font-size: 22px;
    line-height: 28px;
    letter-spacing: 0.3px;
    font-weight: 400;
  }
  .kicker strong {
    font-weight: 700;
  }
  .main-title {
    margin: 6px 0 0;
    font-weight: 400;
    font-size: 100px;
    line-height: 84px;
  }
  .main-title .line-one {
    display: block;
    color: var(--ink-forest);
  }
  .main-title .line-two {
    display: block;
    color: var(--title-white);
  }
  .subtitle {
    margin: 8px 0 0;
    font-size: 30px;
    line-height: 38px;
    font-weight: 400;
    color: var(--ink-forest);
  }
</style>
</head>
<body>
  <main class="book-cover">
    <div class="artwork-field" role="img" aria-label="Cover artwork: a woman's head-and-shoulders silhouette filled with a misty green landscape and a small figure in a yoga pose on a hilltop"></div>

    <header class="title-block">
      <p class="kicker">The Wide Season of a <strong>Modest</strong></p>
      <h1 class="main-title">
        <span class="line-one">Velvet</span>
        <span class="line-two">Sparrow</span>
      </h1>
      <p class="subtitle">Notes on Finding Room<br>for Every Part</p>
    </header>
  </main>
</body>
</html>
```